Building Company Business Card Design

Need a design for a business card:
It needs to have: Name, Phone, Facebook link, Website, email
i would also like a list of works we undertake:
-New Homes
-Extensions, Renovations & Bathrooms
-Decking, Carports, Sheds (Residential and Industrial)
-Carpentry
-Fences, Patios & Pergolas

Name, Phone, Facebook link, Website, email + details of services provided listed in description

```html
<!DOCTYPE html>
<html lang="en">
<head>
<meta charset="utf-8">
<title>Ridgeline Homes – Business Card</title>
<link href="https://fonts.googleapis.com/css2?family=Open+Sans:wght@400;600;700&display=swap" rel="stylesheet">
<style>
  :root {
    --canvas: #e3e3e3;
    --card: #fbfbfb;
    --green: #33b24a;
    --grey: #858585;
    --ink: #1f1f1f;
    --muted: #6f6f6f;
  }
  html, body {
    margin: 0;
    padding: 0;
    width: 1029px;
    height: 1200px;
    overflow: hidden;
    background: var(--canvas);
    font-family: "Open Sans", Arial, sans-serif;
  }
  .stage { position: relative; width: 1029px; height: 1200px; }
  .side-label {
    position: absolute;
    left: 56px;
    font-weight: 700;
    font-size: 17px;
    letter-spacing: 0.5px;
    color: #000;
    transform: rotate(-90deg);
    transform-origin: left top;
  }
  .side-label.front { top: 586px; }
  .side-label.back { top: 1149px; }
  .card {
    position: absolute;
    left: 84px;
    width: 861px;
    height: 506px;
    background:
      radial-gradient(ellipse at 20% 15%, rgba(0,0,0,0.035), transparent 55%),
      radial-gradient(ellipse at 85% 80%, rgba(0,0,0,0.03), transparent 50%),
      var(--card);
    overflow: hidden;
  }
  .card.front { top: 80px; }
  .card.back { top: 642px; }
  .card-shapes { position: absolute; left: 0; top: 0; width: 861px; height: 506px; }

  .brand {
    position: absolute;
    left: 460px;
    top: 295px;
    color: var(--ink);
    font-weight: 600;
  }
  .brand-mark {
    display: block;
    width: 22px;
    height: 22px;
    background: var(--green);
    margin: 0 auto 10px;
  }
  .brand-name { font-size: 31px; line-height: 1; letter-spacing: 0.5px; white-space: nowrap; }
  .brand-sub { font-size: 14.5px; line-height: 1.3; letter-spacing: 0.6px; white-space: nowrap; }

  .person { position: absolute; left: 51px; top: 33px; }
  .person-name { margin: 0; font-size: 38px; line-height: 1.2; color: var(--green); font-weight: 400; }
  .person-name strong { font-weight: 700; }
  .person-role { margin: 0; font-size: 22px; line-height: 1.3; color: var(--muted); }

  .services {
    position: absolute;
    left: 51px;
    top: 137px;
    margin: 0;
    padding: 0;
    list-style: none;
    font-size: 16px;
    color: var(--ink);
  }
  .services li { height: 32px; display: flex; align-items: center; }
  .services svg { width: 12px; height: 10px; margin-right: 9px; flex: none; }

  .contacts {
    position: absolute;
    left: 51px;
    top: 304px;
    margin: 0;
    padding: 0;
    list-style: none;
    font-size: 16px;
    color: var(--ink);
  }
  .contacts li { display: flex; align-items: center; height: 41px; }
  .contacts li.address { height: 46px; }
  .contacts svg { width: 24px; height: 24px; flex: none; margin-right: 11px; }
</style>
</head>
<body>
<div class="stage">

  <span class="side-label front">FRONT</span>
  <section class="card front">
    <svg class="card-shapes" viewBox="0 0 1004 590" aria-hidden="false">
      <defs>
        <linearGradient id="houseTone" x1="0" y1="0" x2="0" y2="1">
          <stop offset="0" stop-color="#5f7fb8"/>
          <stop offset="0.35" stop-color="#3f4a63"/>
          <stop offset="0.7" stop-color="#6a5a48"/>
          <stop offset="1" stop-color="#3f7a2c"/>
        </linearGradient>
      </defs>
      <polygon points="192,59 370,59 256,327 78,327" fill="var(--green)"/>
      <polygon points="322,349 439,349 364,530 222,530" fill="var(--grey)"/>
      <g role="img" aria-label="Photo of a two-storey house with a paved path and lawn at dusk">
        <polygon points="225,103 506,103 340,502 60,502" fill="url(#houseTone)"/>
      </g>
    </svg>
    <div class="brand">
      <span class="brand-mark"></span>
      <div class="brand-name">RIDGELINE HOMES</div>
      <div class="brand-sub">AND DEVELOPMENTS PTY LTD</div>
    </div>
  </section>

  <span class="side-label back">BACK</span>
  <section class="card back">
    <svg class="card-shapes" viewBox="0 0 1004 590">
      <defs>
        <linearGradient id="roomTone" x1="0" y1="0" x2="0" y2="1">
          <stop offset="0" stop-color="#f4efe4"/>
          <stop offset="0.55" stop-color="#e2d3bb"/>
          <stop offset="0.75" stop-color="#c58c55"/>
          <stop offset="1" stop-color="#a8693a"/>
        </linearGradient>
      </defs>
      <polygon points="667,102 817,102 720,321 578,321" fill="var(--green)"/>
      <polygon points="800,339 873,339 812,488 696,488" fill="var(--grey)"/>
      <g role="img" aria-label="Photo of a bright hallway with timber floor, rug and front door">
        <polygon points="699,137 929,137 792,465 562,465" fill="url(#roomTone)"/>
      </g>
    </svg>

    <div class="person">
      <h1 class="person-name"><strong>Your</strong> Name</h1>
      <p class="person-role">Development</p>
    </div>

    <ul class="services">
      <li><svg viewBox="0 0 12 10"><path d="M0 4h7V1l5 4-5 4V6H0z" fill="var(--green)"/></svg>New Homes</li>
      <li><svg viewBox="0 0 12 10"><path d="M0 4h7V1l5 4-5 4V6H0z" fill="var(--green)"/></svg>Extensions, Renovations &amp; Bathrooms</li>
      <li><svg viewBox="0 0 12 10"><path d="M0 4h7V1l5 4-5 4V6H0z" fill="var(--green)"/></svg>Decking, Carports, Sheds (Residential and Industrial)</li>
      <li><svg viewBox="0 0 12 10"><path d="M0 4h7V1l5 4-5 4V6H0z" fill="var(--green)"/></svg>Carpentry</li>
      <li><svg viewBox="0 0 12 10"><path d="M0 4h7V1l5 4-5 4V6H0z" fill="var(--green)"/></svg>Fences, Patios &amp; Pergolas</li>
    </ul>

    <ul class="contacts">
      <li>
        <svg viewBox="0 0 24 24"><path d="M6.6 2.5l3 3.4c.5.6.5 1.4 0 2l-1.7 1.8c1.3 2.6 3.5 4.8 6.1 6.1l1.8-1.7c.6-.5 1.4-.5 2 0l3.4 3c.6.6.6 1.5 0 2.1l-1.7 1.9c-.8.8-2 1.1-3.1.7C9.6 19.9 4.1 14.4 2.2 7.6c-.3-1.1 0-2.3.8-3.1l1.5-1.9c.6-.7 1.6-.7 2.1-.1z" fill="var(--green)"/></svg>
        +123-4567-890
      </li>
      <li>
        <svg viewBox="0 0 24 24" fill="none" stroke="var(--green)" stroke-width="1.8"><circle cx="12" cy="12" r="10"/><ellipse cx="12" cy="12" rx="4.2" ry="10"/><path d="M2 12h20M3.5 7h17M3.5 17h17"/></svg>
        www.yourwebsite.com
      </li>
      <li>
        <svg viewBox="0 0 24 24"><rect x="1" y="5" width="22" height="14" fill="var(--green)"/><path d="M1.5 5.5L12 13l10.5-7.5" fill="none" stroke="#fff" stroke-width="1.6"/></svg>
        hello@youremail.com
      </li>
      <li class="address">
        <svg viewBox="0 0 24 24"><path d="M12 1a8 8 0 0 0-8 8c0 6 8 14 8 14s8-8 8-14a8 8 0 0 0-8-8z" fill="var(--green)"/><circle cx="12" cy="9" r="3" fill="#fff"/></svg>
        123 Anywhere St.,. Any City
      </li>
    </ul>
  </section>

</div>
</body>
</html>
```